Label Design for RTD Cocktail Line Tovelin Spirits

Tovelin Spirits is a line of Indian-inspired artisan cocktails that "brings the bartender home" for professional men and women who like the finer things in life but don’t always have the time to treat themselves. No need for a multitude of expensive and hard-to-find ingredients, time consuming recipes, or a mixologist.

Our line of 3 open and serve cocktails blends a range of premium spirits with exotic ingredients so you can conveniently raise a glass for any of life’s celebrations.

Our bottle is the 750ml Claret bottle with Quarnet (screw cap) closure and will be covered entirely in a shrink sleeve (so potentially anything can be designed for any part of the bottle). We want the bottle to pop on the shelf so it should look different than what’s already out there (Velvet Moth, Galdrova, Merlusa ready to drink cocktails). We are looking for a sexy design that's polished/sleek.
Updates

Project Deadline Extended
Reason: Hello designers! Tovelin Spirits is so impressed with what we have received thus far and we would like to give some of the designers a few extra days to make the edits we requested. It's never too late to submit! Thank you all!

Industry/Entity Type

It Professional

Requirements
Must have
• Front of bottle
* “Tovelin Spirits” name and Peacock Logo- but feel free to pull the elements apart and use them on the bottle in different ways
* Open & Serve
* 12% ALC/VOL
* 750 ml
* 3 different labels in a theme for
-Borvelle
-Faluntera
-Pomadrine

Borvelle Ideas- soft brown palate, the ingredients in chai spice (cloves, cardamom pods, nutmeg, black peppercorns, star anise, and cinnamon stick)

Faluntera Ideas -cool and refreshing, pale green shade (not clashing with logo), graphics of fresh mint leaves, green chili, lime, cucumber

Pomadrine Ideas- soft/pale pink shades, graphics of lychi fruit (outer red shell and inner pink flesh), ginger

Back of bottle
* explanation of the 3 cocktails
Borvelle: Forget what you think you know about chai, this is not the Queen’s tea-time drink! Borvelle is a smooth, sweetly -spiced cocktail made with vodka, black tea, and a combination of aromatic spices. This velvety cocktail is rich without being heavy. Enjoy chilled or over ice anytime.

Faluntera: Faluntera can’t make up its mind! This fusion of zesty lime, sweet mint, earthy cucumber and spicy chilies is so refreshing you’ll crave it on a hot summer day or a cool winter’s night. The exotic botanicals in gin add a complexity to the cocktail making this a refreshing but potent drink! Enjoy chilled or over ice anytime.

Pomadrine: East meet West. Delicate lychi meet hard-hitting whiskey. Pomadrine will tempt you senses with flavor, fragrance and beauty. The peppery kick of ginger and the intensity of the un-aged whiskey are softened by lychi’s intoxicating scent and subtle, sweet finish.

Please include
1. Bottled By QRW Spirits Company
2. Sample barcode (where you would place it in your design)
3. www.TovelinSpirits.example
4. GOVERNMENT WARNING: (1) According to the Surgeon General, women should not drink alcoholic beverages during pregnancy because of the risk of birth defects. (2) Consumption of alcoholic beverages impairs your ability to drive a car or operate machinery, and may cause health problems.

Optional to include
*"Bring the Bartender Home"
*"Tovelin Spirits” name and Peacock Logo on the back
*Entirely black sleeve with contrasting design

FYI the Fonts used in our logo are Geosans Light and Prakrta, but feel free to use other complimentary fonts on the other aspects.
Nice to have
• Optional to include

```html
<!DOCTYPE html>
<html lang="en">
<head>
<meta charset="utf-8">
<title>Tovelin Spirits — Borvelle Label</title>
<link rel="stylesheet" href="https://fonts.googleapis.com/css2?family=Cinzel:wght@400;600;700&family=Arimo:wght@400&display=swap">
<style>
  :root {
    --maroon: #6c0f26;
    --maroon-deep: #4e0a1b;
    --maroon-soft: #8a1a32;
    --gold: #dcb878;
    --cream: #f7f0d8;
    --cream-edge: #efe4c2;
    --spice-brown: #7a2a2c;
  }
  * { box-sizing: border-box; margin: 0; padding: 0; }
  html, body { width: 934px; height: 1200px; overflow: hidden; background: var(--cream-edge); }
  .sleeve {
    position: relative;
    width: 934px;
    height: 1200px;
    background: linear-gradient(90deg, var(--cream-edge) 0%, var(--cream) 30%, var(--cream) 70%, var(--cream-edge) 100%);
    overflow: hidden;
  }
  .cap-band {
    position: absolute;
    left: 0; top: 0;
    width: 934px; height: 150px;
    background: linear-gradient(90deg, var(--maroon-deep), var(--maroon) 40%, var(--maroon-soft) 70%, var(--maroon-deep));
    display: flex;
    align-items: flex-end;
    justify-content: center;
    padding-bottom: 14px;
  }
  .cap-name {
    font-family: "Cinzel", serif;
    font-weight: 600;
    font-size: 40px;
    letter-spacing: 6px;
    color: var(--maroon-soft);
    filter: brightness(1.35);
  }
  .crest {
    position: absolute;
    left: 297px; top: 330px;
    width: 340px; height: 350px;
  }
  .crest-name {
    position: absolute;
    left: 0; top: 110px;
    width: 340px;
    text-align: center;
    font-family: "Cinzel", serif;
    font-weight: 600;
    font-size: 40px;
    line-height: 1.15;
    letter-spacing: 2px;
    color: var(--gold);
  }
  .ribbon {
    position: absolute;
    left: 177px; top: 630px;
    width: 580px; height: 120px;
  }
  .spice-cluster {
    position: absolute;
    left: 347px; top: 735px;
    width: 240px; height: 95px;
    background: radial-gradient(ellipse at center, var(--spice-brown) 0%, var(--maroon) 55%, rgba(108,15,38,0) 72%);
    border-radius: 50%;
  }
  .serve-line {
    position: absolute;
    left: 217px; top: 790px;
    width: 500px; height: 130px;
  }
  .strength, .volume {
    position: absolute;
    left: 0; width: 934px;
    text-align: center;
    font-family: "Arimo", sans-serif;
    font-size: 19px;
    color: var(--maroon);
  }
  .strength { top: 930px; }
  .volume { top: 962px; }
</style>
</head>
<body>
  <main class="sleeve">
    <div class="cap-band">
      <span class="cap-name">TOVELIN</span>
    </div>

    <div class="crest">
      <svg width="340" height="350" viewBox="0 0 340 350" aria-hidden="true">
        <path d="M0 0 H340 V190 Q340 310 170 350 Q0 310 0 190 Z" fill="var(--maroon)"/>
      </svg>
      <div class="crest-name">Tovelin<br>Spirits</div>
    </div>

    <svg class="ribbon" viewBox="0 0 580 120" aria-hidden="true">
      <path d="M0 38 L60 34 L60 104 L0 108 L22 72 Z" fill="var(--maroon-deep)"/>
      <path d="M580 38 L520 34 L520 104 L580 108 L558 72 Z" fill="var(--maroon-deep)"/>
      <path d="M30 20 Q290 -4 550 20 L550 92 Q290 68 30 92 Z" fill="var(--maroon)"/>
      <text x="290" y="72" text-anchor="middle" font-family="Cinzel, serif" font-weight="600" font-size="52" letter-spacing="2" fill="var(--gold)">BORVELLE</text>
    </svg>

    <div class="spice-cluster" role="img" aria-label="Illustration of chai spices: cinnamon sticks, star anise and cloves"></div>

    <svg class="serve-line" viewBox="0 0 500 130" aria-hidden="true">
      <path id="serve-arc" d="M40 40 Q250 140 460 40" fill="none"/>
      <text font-family="Cinzel, serif" font-weight="700" font-size="44" letter-spacing="2" fill="var(--gold)">
        <textPath href="#serve-arc" startOffset="50%" text-anchor="middle">Open &amp; Serve</textPath>
      </text>
    </svg>

    <p class="strength">12% ALC/VOL</p>
    <p class="volume">750 ml</p>
  </main>
</body>
</html>
```